Menu Board and Flyer for a Poke Restaurant

We need for our new Menu board for a Poke restaurant. There will be 2 separate boards. 1 Board for Speciality items, the second for "Build your Own". The menu boards will be installed on a wall.

The first board is going to be 36 W x 48 H inches. The second board will be 72 W x 48 H inches.

I would also like to consolidate the board into a one Page menu flyer that can be printed on an 11 inches x 14 inches Page.

The goal is to have customers focus on the ease of ordering.
We have attached a sample design idea for reference and our logo options. Including the logo is optional.

I have included some sample menus by other companies as attachment and referance.

Files need to include any special fonts used in the design.

Target Market(s)

Young Professionals who love eating healthy, trendy, delicious new food options.

Industry/Entity Type

Fast Food Restaurant

Font styles to use
Serif
Sans Serif

Requirements
Must have
• Simple
• Clean design - NOT busy
• Fun
• Easy to follow
• Highlight a step by step ordering process.
• Light background color
• Files need to include any special fonts used in the design.
Should not have
• script fonts

```html
<!DOCTYPE html>
<html lang="en">
<head>
<meta charset="utf-8">
<title>Tidewater Pokehouse – Build Your Own</title>
<link href="https://fonts.googleapis.com/css2?family=Bebas+Neue&family=Oswald:wght@300;400&family=Open+Sans:ital@1&display=swap" rel="stylesheet">
<style>
  :root{
    --bg:#dde6ec;
    --paper:#f3f6f8;
    --sky:#8fcbe2;
    --sky-soft:#bfe0ec;
    --ink:#5f6b73;
    --shadow:#56636b;
    --rule:#d3dde3;
    --deco:#cfdde5;
  }
  *{margin:0;padding:0;box-sizing:border-box}
  html,body{width:1200px;height:900px;overflow:hidden;background:var(--bg)}
  .menu-board{position:relative;width:1200px;height:900px;overflow:hidden;background:var(--bg);font-family:"Oswald",sans-serif}

  .brand{position:absolute;left:34px;top:30px;width:200px;height:150px;display:flex;align-items:center;gap:10px}
  .brand-dot{width:16px;height:16px;border-radius:50%;background:var(--sky);flex:none}
  .brand-name{font-family:"Oswald",sans-serif;font-weight:300;font-size:28px;line-height:1.05;color:var(--sky);text-transform:uppercase;letter-spacing:1px}

  .headline{position:absolute;left:292px;top:34px;width:870px;font-family:"Bebas Neue",sans-serif;font-weight:400;font-size:150px;line-height:1;letter-spacing:4px;color:var(--sky-soft);text-shadow:6px 6px 0 var(--shadow);white-space:nowrap}

  .paper{position:absolute;left:18px;top:200px;width:1164px;height:682px}
  .paper svg{width:100%;height:100%;display:block}

  .divider{position:absolute;top:420px;width:1px;height:460px;background:var(--rule)}

  .flow{position:absolute;left:0;top:240px;width:1200px;height:60px}

  .step{position:absolute;top:240px;width:170px;height:170px;margin-left:-85px;text-align:center;color:var(--sky)}
  .step-ring{position:absolute;left:10px;top:10px;width:150px;height:150px}
  .step-kicker{position:absolute;left:0;right:0;top:42px;font-family:"Oswald",sans-serif;font-weight:300;font-size:19px;letter-spacing:1px;text-transform:uppercase}
  .step-title{position:absolute;left:-20px;right:-20px;top:62px;display:flex;justify-content:center;align-items:flex-end;font-family:"Bebas Neue",sans-serif;white-space:nowrap}
  .step-num{font-size:86px;line-height:.8;margin-right:6px}
  .step-word{font-size:58px;line-height:.85;letter-spacing:1px}

  .options{position:absolute;top:430px;list-style:none}
  .options li{display:flex;font-family:"Oswald",sans-serif;font-weight:300;font-size:22px;line-height:33px;color:var(--ink);text-transform:uppercase;letter-spacing:.5px}
  .options .n{color:var(--sky);width:28px;flex:none}
  .options .wide{width:34px}
  .style-list li{flex-wrap:wrap;line-height:28px;margin-bottom:14px}
  .style-list .note{display:block;width:100%;padding-left:28px;font-family:"Open Sans",sans-serif;font-style:italic;font-size:13px;line-height:16px;color:var(--sky);text-transform:none;letter-spacing:0}

  .deco{position:absolute;top:740px;width:100px;height:90px;border-radius:46px;background:var(--deco);opacity:.6}
</style>
</head>
<body>
<main class="menu-board">

  <div class="brand">
    <span class="brand-dot"></span>
    <span class="brand-name">Tidewater<br>Pokehouse</span>
  </div>

  <h1 class="headline">BUILD YOUR OWN</h1>

  <div class="paper">
    <svg viewBox="0 0 1164 682" preserveAspectRatio="none" aria-hidden="true">
      <path d="M0 14 Q60 4 130 12 T270 10 T420 14 T580 8 T740 13 T900 9 T1060 14 T1164 10 L1164 682 L0 682 Z" fill="var(--paper)"/>
      <path d="M0 8 Q70 -2 150 8 T320 6 T500 10 T680 4 T860 9 T1040 5 T1164 8" fill="none" stroke="var(--sky-soft)" stroke-width="4"/>
    </svg>
  </div>

  <span class="divider" style="left:248px"></span>
  <span class="divider" style="left:483px"></span>
  <span class="divider" style="left:725px"></span>
  <span class="divider" style="left:960px"></span>

  <svg class="flow" viewBox="0 0 1200 60" aria-hidden="true">
    <g fill="none" stroke="var(--sky)" stroke-width="3" stroke-linecap="round" stroke-linejoin="round">
      <path d="M218 38 Q250 18 286 28"/><path d="M276 20 L288 28 L276 36"/>
      <path d="M462 38 Q494 18 530 28"/><path d="M520 20 L532 28 L520 36"/>
      <path d="M712 38 Q744 18 780 28"/><path d="M770 20 L782 28 L770 36"/>
      <path d="M946 38 Q978 18 1014 28"/><path d="M1004 20 L1016 28 L1004 36"/>
    </g>
  </svg>

  <div class="step" style="left:118px">
    <svg class="step-ring" viewBox="0 0 150 150" aria-hidden="true"><circle cx="75" cy="75" r="71" fill="none" stroke="var(--sky-soft)" stroke-width="3"/></svg>
    <span class="step-kicker">Choose your</span>
    <div class="step-title"><span class="step-num">1</span><span class="step-word">STYLE</span></div>
  </div>
  <div class="step" style="left:382px">
    <svg class="step-ring" viewBox="0 0 150 150" aria-hidden="true"><circle cx="75" cy="75" r="71" fill="none" stroke="var(--sky-soft)" stroke-width="3"/></svg>
    <span class="step-kicker">Choose your</span>
    <div class="step-title"><span class="step-num">2</span><span class="step-word">PROTEIN</span></div>
  </div>
  <div class="step" style="left:624px">
    <svg class="step-ring" viewBox="0 0 150 150" aria-hidden="true"><circle cx="75" cy="75" r="71" fill="none" stroke="var(--sky-soft)" stroke-width="3"/></svg>
    <span class="step-kicker">Choose your</span>
    <div class="step-title"><span class="step-num">3</span><span class="step-word">TOPPINS</span></div>
  </div>
  <div class="step" style="left:858px">
    <svg class="step-ring" viewBox="0 0 150 150" aria-hidden="true"><circle cx="75" cy="75" r="71" fill="none" stroke="var(--sky-soft)" stroke-width="3"/></svg>
    <span class="step-kicker">Choose your</span>
    <div class="step-title"><span class="step-num">4</span><span class="step-word">SOUCE</span></div>
  </div>
  <div class="step" style="left:1080px">
    <svg class="step-ring" viewBox="0 0 150 150" aria-hidden="true"><circle cx="75" cy="75" r="71" fill="none" stroke="var(--sky-soft)" stroke-width="3"/></svg>
    <span class="step-kicker">Choose your</span>
    <div class="step-title"><span class="step-num">5</span><span class="step-word">BASE</span></div>
  </div>

  <ol class="options style-list" style="left:48px">
    <li><span class="n">1</span>Classic Bowl<span class="note">Regular or Large</span></li>
    <li><span class="n">2</span>Crunchy Bowl<span class="note">One size, Tostada Style</span></li>
    <li><span class="n">3</span>Surfer Style<span class="note">Poke served taco style</span></li>
    <li><span class="n">4</span>Classic Bowl<span class="note">no base -<br>1lb of your favorite poke</span></li>
  </ol>

  <ol class="options" style="left:286px">
    <li><span class="n">1</span>Ahi</li>
    <li><span class="n">2</span>Tuna</li>
    <li><span class="n">3</span>Salmon</li>
    <li><span class="n">4</span>Hamachi</li>
    <li><span class="n">5</span>Spicy Tuna</li>
    <li><span class="n">6</span>Scallop</li>
    <li><span class="n">7</span>Shrimp</li>
  </ol>

  <ol class="options" style="left:526px">
    <li><span class="n wide">1</span>Crispy Onion</li>
    <li><span class="n wide">2</span>Green Onion</li>
    <li><span class="n wide">3</span>Sweet Onion</li>
    <li><span class="n wide">4</span>Masago</li>
    <li><span class="n wide">5</span>Cilantro</li>
    <li><span class="n wide">6</span>Cucumber</li>
    <li><span class="n wide">7</span>Corn</li>
    <li><span class="n wide">8</span>Coconut Flakes</li>
    <li><span class="n wide">9</span>Ogo</li>
    <li><span class="n wide">10</span>Furikake</li>
    <li><span class="n wide">11</span>Panko</li>
    <li><span class="n wide">12</span>Sesame Seed</li>
    <li><span class="n wide">13</span>Avocado</li>
  </ol>

  <ol class="options" style="left:768px">
    <li><span class="n">1</span>Sesame Shoyu</li>
    <li><span class="n">2</span>Sriracha Aioli</li>
    <li><span class="n">3</span>Ponzu</li>
    <li><span class="n">4</span>Sweet Shoyu</li>
    <li><span class="n">5</span>Wasabi Shoyu</li>
    <li><span class="n">6</span>Sweet Chili</li>
    <li><span class="n">7</span>Chili Lime</li>
    <li><span class="n">8</span>Ginger-Scallion</li>
    <li><span class="n">9</span>Wasabi Creme</li>
  </ol>

  <ol class="options" style="left:1000px">
    <li><span class="n">1</span>White Rice</li>
    <li><span class="n">2</span>Brown Rice</li>
    <li><span class="n">3</span>Black Rice</li>
    <li><span class="n">4</span>Mixed Greens</li>
  </ol>

  <div class="deco" style="left:80px" role="img" aria-label="Faint compass rose decoration"></div>
  <div class="deco" style="left:300px;width:120px" role="img" aria-label="Faint leaping dolphin over waves decoration"></div>
  <div class="deco" style="left:680px;width:40px;top:762px;height:40px" role="img" aria-label="Faint starfish decoration"></div>
  <div class="deco" style="left:810px;width:80px;top:770px;height:40px" role="img" aria-label="Faint wave lines decoration"></div>
  <div class="deco" style="left:1030px;width:90px" role="img" aria-label="Faint seashell decoration"></div>

</main>
</body>
</html>
```